RLT PowerPoint

I am looking for a clean, corporate PowerPoint template.

I would like the following:
- title slide
- break slide
- blank slide with title (for graphs or graphics)
- an ending slide.

Target Market(s)

Business professionals, medium to large business clients.

Requirements
Must have
• Must incorporate the RLT logo in either the header or footer

```html
<!DOCTYPE html>
<html lang="en">
<head>
<meta charset="utf-8">
<title>RLT – Graphic Slide</title>
<link rel="stylesheet" href="https://fonts.googleapis.com/css2?family=Graduate&family=PT+Sans:wght@400;700&display=swap">
<style>
  :root {
    --page: #ffffff;
    --slide-light: #f2f2f2;
    --slide-mid: #d9d9d9;
    --ink: #333333;
    --bar: #222222;
    --blue: #25a8e0;
    --blue-dark: #1874bb;
    --green-light: #8dc63f;
    --green-light-dark: #5fa83a;
    --green-dark: #0d9447;
    --green: #30b36f;
    --teal: #13a89e;
    --tan: #c49a6c;
    --tan-dark: #a97c50;
    --grey: #6d6e71;
    --grey-dark: #3f3f41;
    --pyramid-grey: #58585a;
    --pyramid-grey-dark: #3b3b3d;
    --white: #ffffff;
  }
  html, body { margin: 0; padding: 0; overflow: hidden; }
  body { width: 1200px; height: 900px; background: var(--page); position: relative; font-family: "PT Sans", sans-serif; }
  .slide {
    position: absolute; left: 27px; top: 183px; width: 1146px; height: 645px;
    background: radial-gradient(ellipse at 40% 40%, var(--slide-light), var(--slide-mid));
    overflow: hidden;
  }
  .slide-art { position: absolute; left: 0; top: 0; }
  .page-number {
    position: absolute; right: 28px; top: 32px; margin: 0;
    font-family: "Graduate", serif; font-size: 22px; color: var(--white); letter-spacing: 1px;
  }
  .title-bar {
    position: absolute; left: 16px; top: 490px; width: 1115px; height: 143px; background: var(--bar);
  }
  .slide-title {
    position: absolute; left: 22px; top: 12px; margin: 0;
    font-family: "Graduate", serif; font-weight: 400; font-size: 66px; line-height: 1;
    color: var(--blue); letter-spacing: 1px; transform: scaleY(1.08); transform-origin: top left;
  }
  .title-rule { position: absolute; left: 24px; top: 93px; width: 503px; height: 3px; background: var(--white); }
  .slide-subtitle {
    position: absolute; left: 80px; top: 103px; margin: 0;
    font-size: 18px; color: var(--white); letter-spacing: 0.3px;
  }
  .contact {
    position: absolute; right: 173px; top: 59px; margin: 0; text-align: right;
    font-size: 11px; line-height: 17px; color: var(--white); letter-spacing: 0.3px;
  }
  .brand-box {
    position: absolute; right: 16px; top: 10px; width: 147px; height: 123px; background: var(--white);
    display: flex; align-items: center; justify-content: center;
  }
  .brand-name { font-family: "PT Sans", sans-serif; font-weight: 700; font-size: 52px; color: var(--blue-dark); letter-spacing: 1px; }
</style>
</head>
<body>
<section class="slide">
  <svg class="slide-art" width="1146" height="645" viewBox="27 183 1146 645" aria-hidden="true">
    <!-- progress track -->
    <line x1="95" y1="242" x2="1033" y2="242" stroke="var(--ink)" stroke-width="4"/>
    <rect x="58" y="227" width="30" height="30" rx="5" transform="rotate(45 73 242)" fill="var(--white)" stroke="var(--ink)" stroke-width="3"/>
    <circle cx="73" cy="242" r="8" fill="var(--blue)"/>
    <!-- page corner -->
    <polygon points="1057,196 1158,196 1158,298" fill="var(--blue)"/>

    <!-- pyramid -->
    <polygon class="tier-top" points="337,369 400,438 275,438" fill="var(--green-light)"/>
    <polygon points="275,438 400,438 394,450 281,450" fill="var(--green-light-dark)"/>
    <polygon class="tier-middle" points="263,450 409,450 480,523 192,523" fill="var(--blue)"/>
    <polygon points="192,523 480,523 470,533 202,533" fill="var(--blue-dark)"/>
    <polygon class="tier-base" points="152,533 522,533 565,605 108,605" fill="var(--pyramid-grey)"/>
    <polygon points="108,605 565,605 545,633 128,633" fill="var(--pyramid-grey-dark)"/>

    <!-- pie chart depth -->
    <g transform="translate(0 24)">
      <path d="M853 470 L1019 470 A166 166 0 0 1 931 617 Z" fill="var(--blue-dark)"/>
      <path d="M853 470 L931 617 A166 166 0 0 1 775 617 Z" fill="var(--tan-dark)"/>
      <path d="M853 470 L775 617 A166 166 0 0 1 687 470 Z" fill="var(--grey-dark)"/>
    </g>
    <!-- pie chart -->
    <g stroke="#000" stroke-width="4" stroke-linejoin="round">
      <path d="M853 470 L751 339 A166 166 0 0 1 853 304 Z" fill="var(--green-dark)"/>
      <path d="M853 470 L853 304 A166 166 0 0 1 984 368 Z" fill="var(--green)"/>
      <path d="M853 470 L984 368 A166 166 0 0 1 1019 470 Z" fill="var(--teal)"/>
      <path d="M853 470 L1019 470 A166 166 0 0 1 931 617 Z" fill="var(--blue)"/>
      <path d="M853 470 L931 617 A166 166 0 0 1 775 617 Z" fill="var(--tan)"/>
      <path d="M853 470 L775 617 A166 166 0 0 1 687 470 Z" fill="var(--grey)"/>
      <path d="M853 470 L687 470 A166 166 0 0 1 751 339 Z" fill="var(--green-light)"/>
    </g>
  </svg>

  <p class="page-number">04</p>

  <footer class="title-bar">
    <h1 class="slide-title">GRAPHIC SLIDE</h1>
    <div class="title-rule"></div>
    <p class="slide-subtitle">DETAILS OF SLIDE / NAME OF PRESENTOR</p>
    <p class="contact">WWW.COMPANYSITE.COM<br>COMPANY@COMPANY.COM</p>
    <div class="brand-box"><span class="brand-name">RLT</span></div>
  </footer>
</section>
</body>
</html>
```